Hip surgeon needs a stationery design

I need a new stationery design for my private practice.
My practice is focused in hip arthroplasty (hip prosthesis).
I'd like to see designs most in blue or shades of blue.
I've uploaded my new logo to help with the task.
Also, I'm a member of some societies and I've uploaded their logos either, so I'd like to see them in some of the stationeries.
Itens list:
business card
letterhead A4
envelope
prescription block A5
one fold for A4 (please see the archive "pocket")
Personal data:
Dr. Renan L. Vasconti
CRM/PR 57316
site: www.clinicapelvora.com.br
email: dr.renan@clinicapelvora.com.br
Adress:
Rua Leopoldo Marques Vieira de Lima, 712
Campo Sereno - Curitiba/PR
41 30875316 I 30875317
Updates
I forgot to mention that my practice is focused primarily in hip arthroplasty (total hip prosthesis) and the target audience range from young adults to the elderly.
I also perform hip preserving surgeries (open and arthroscopic procedures) and pelvic and hip fracture surgery (trauma).
- Any "cleaner" fonts are welcome

```html
<!DOCTYPE html>
<html lang="pt-BR">
<head>
<meta charset="utf-8">
<title>Cartão de visita — Dr. Renan L. Vasconti</title>
<link href="https://fonts.googleapis.com/css2?family=Open+Sans:wght@400;600&display=swap" rel="stylesheet">
<style>
  :root {
    --backdrop: #d3e1e5;
    --paper: #ffffff;
    --brand-blue: #2b7cc0;
    --ink: #2e2e30;
    --ink-soft: #6f7276;
    --ghost: #e6e9f3;
    --edge-shadow: rgba(40, 60, 70, 0.28);
  }
  * { box-sizing: border-box; margin: 0; padding: 0; }
  html, body {
    width: 1200px; height: 1000px; overflow: hidden;
    background: var(--backdrop);
    font-family: "Open Sans", Arial, sans-serif;
  }
  .stage { position: relative; width: 1200px; height: 1000px; }

  .card {
    position: absolute;
    width: 500px; height: 290px;
    background: var(--paper);
    overflow: hidden;
    box-shadow: 0 3px 0 #3c3f42, 0 12px 28px var(--edge-shadow);
  }
  .card--front { left: 150px; top: 120px; }
  .card--back  { left: 560px; top: 560px; }

  .brand {
    display: flex; align-items: center; gap: 10px;
    color: var(--brand-blue);
    font-weight: 600; font-size: 22px; letter-spacing: 0.2px;
  }
  .brand__dot {
    width: 30px; height: 30px; border-radius: 50%;
    background: var(--brand-blue); flex: none;
  }
  .card--front .brand {
    position: absolute; left: 50%; top: 50%;
    transform: translate(-50%, -50%);
  }
  .card--back .brand { position: absolute; left: 120px; top: 60px; }

  .ghost-circle {
    position: absolute; right: -70px; top: 20px;
    width: 240px; height: 240px; border-radius: 50%;
    background: var(--ghost);
  }

  .holder { position: absolute; left: 110px; bottom: 62px; }
  .holder__name { font-size: 22px; color: var(--ink); font-weight: 400; }
  .holder__reg { font-size: 13px; color: var(--ink-soft); margin: 3px 0 0 56px; letter-spacing: 0.4px; }

  .contact {
    position: absolute; left: 300px; top: 118px;
    list-style: none; font-size: 7.5px; color: var(--ink-soft); line-height: 1.35;
  }
  .contact li { display: flex; align-items: flex-start; gap: 4px; }
  .contact svg { flex: none; margin-top: 1px; }
  .contact .indent { padding-left: 12px; }
</style>
</head>
<body>
<main class="stage">
  <section class="card card--front" aria-label="Frente do cartão">
    <div class="brand"><span class="brand__dot"></span>Clínica Pelvora</div>
  </section>

  <section class="card card--back" aria-label="Verso do cartão">
    <div class="ghost-circle" role="img" aria-label="Elemento decorativo suave da marca"></div>
    <div class="brand"><span class="brand__dot"></span>Clínica Pelvora</div>

    <ul class="contact">
      <li>
        <svg width="8" height="8" viewBox="0 0 8 8"><circle cx="4" cy="4" r="4" fill="var(--brand-blue)"/><circle cx="4" cy="3.4" r="1.3" fill="#fff"/></svg>
        Rua Leopoldo Marques Vieira de Lima, 712
      </li>
      <li class="indent">Campo Sereno - Curitiba/PR</li>
      <li>
        <svg width="8" height="8" viewBox="0 0 8 8"><circle cx="4" cy="4" r="4" fill="var(--brand-blue)"/><rect x="2.6" y="2" width="2.8" height="4" rx="0.6" fill="#fff"/></svg>
        41 30875316 I 30875317
      </li>
      <li>
        <svg width="8" height="8" viewBox="0 0 8 8"><circle cx="4" cy="4" r="4" fill="var(--brand-blue)"/><circle cx="4" cy="4" r="2" fill="none" stroke="#fff" stroke-width="0.7"/></svg>
        www.clinicapelvora.com.br
      </li>
      <li>
        <svg width="8" height="8" viewBox="0 0 8 8"><circle cx="4" cy="4" r="4" fill="var(--brand-blue)"/><rect x="2" y="2.7" width="4" height="2.6" fill="#fff"/></svg>
        dr.renan@clinicapelvora.com.br
      </li>
    </ul>

    <div class="holder">
      <p class="holder__name">Dr. Renan L. Vasconti</p>
      <p class="holder__reg">CRM/PR 57316</p>
    </div>
  </section>
</main>
</body>
</html>
```